Pet store web design

I would like to redesign my current online store (http://brindlecorner.com)
I'm looking for a clean, modern design. Any ideas are welcome..

Industry/Entity Type

Pet

Number of Pages Required

3 page

```html
<!DOCTYPE html>
<html lang="en">
<head>
<meta charset="utf-8">
<title>Brindle Corner – Pet Store</title>
<link href="https://fonts.googleapis.com/css2?family=Raleway:wght@400;500;600;700;800&family=Open+Sans:wght@400;600;700&display=swap" rel="stylesheet">
<style>
:root{
  --teal:#1f9aa0;
  --teal-dark:#17858a;
  --ink:#333;
  --muted:#888;
  --line:#e3e3e3;
  --hero:#eeeeee;
  --yellow:#f5c315;
  --blue:#1eb1e3;
  --tan:#d9a077;
  --red:#df5b5b;
  --grey:#7d7d7d;
  --cream:#f3efe3;
  --price:#555;
}
*{box-sizing:border-box;margin:0;padding:0}
html,body{width:1200px;height:2612px;overflow:hidden;background:#fff}
body{font-family:"Open Sans",Arial,sans-serif;color:var(--ink);position:relative}
a{color:inherit;text-decoration:none}
.abs{position:absolute}

/* top bar */
.topbar{position:absolute;top:0;left:0;width:1200px;height:100px}
.toplinks{left:100px;top:42px;font-size:13px;color:#555;display:flex;gap:18px}
.brand{left:500px;top:16px;width:200px;height:66px;display:flex;align-items:center;justify-content:center;gap:10px;font-family:"Raleway",sans-serif;font-weight:800;font-size:24px;color:var(--teal)}
.brand .dot{width:18px;height:18px;background:var(--yellow);border-radius:50%}
.account{left:850px;top:42px;font-size:12px;color:#555;display:flex;gap:14px;align-items:center}
.cart{font-weight:700;color:var(--ink);font-size:15px;display:flex;gap:6px;align-items:center}

/* nav */
.nav{top:104px;left:0;width:1200px;height:44px;border-top:1px solid var(--line);border-bottom:1px solid var(--line)}
.nav ul{position:absolute;left:100px;top:12px;list-style:none;display:flex;gap:44px;font-family:"Raleway",sans-serif;font-size:13px;font-weight:700;color:#444}
.nav li.active{color:var(--teal)}
.search{position:absolute;right:100px;top:8px;width:190px;height:26px;border:1px solid #ddd;border-radius:13px;font-size:11px;color:#aaa;padding:5px 0 0 28px}
.search svg{position:absolute;left:9px;top:6px}

/* hero */
.hero{top:148px;left:0;width:1200px;height:592px;background:var(--hero);border-bottom:5px solid var(--yellow)}
.hero-photo{position:absolute;left:330px;top:0;width:780px;height:587px;background:radial-gradient(ellipse at 60% 55%,#c79a62 0%,#a77847 35%,#d9d4cc 70%,var(--hero) 100%)}
.hero-copy{position:absolute;left:100px;top:220px;font-family:"Raleway",sans-serif}
.hero-copy h1{font-size:42px;font-weight:700;color:var(--teal);letter-spacing:.5px}
.hero-copy h2{font-size:21px;font-weight:700;color:#333;line-height:30px;margin-top:6px}
.hero-copy .deal{font-size:19px;font-weight:500;color:#444;margin-top:6px}
.hero-copy .tag{font-size:16px;color:#e0b100;margin-top:8px}
.btn{display:inline-block;background:var(--teal);color:#fff;font-size:12px;font-weight:700;border-radius:18px;padding:10px 30px;margin-top:22px;font-family:"Raleway",sans-serif}
.arrow{position:absolute;top:240px}

/* features */
.features{top:800px;left:100px;width:1000px;display:flex;gap:32px}
.feature{width:226px;height:80px;display:flex;align-items:center;gap:14px;padding:0 18px;color:#fff;font-size:13px;font-weight:600;line-height:17px}
.feature svg{flex:none}
.f-blue{background:var(--blue)}.f-tan{background:var(--tan)}.f-red{background:var(--red)}.f-grey{background:var(--grey)}

/* tabs */
.tabs{top:980px;left:100px;width:1000px;height:40px}
.tabs .rule{position:absolute;top:20px;height:1px;background:var(--line);width:200px}
.tabs ul{position:absolute;left:225px;width:550px;list-style:none;display:flex;justify-content:space-around;font-family:"Raleway",sans-serif;font-size:22px;font-weight:500;color:#666;top:4px}
.tabs li.active{color:var(--teal);border-bottom:2px solid var(--teal);padding-bottom:4px}

/* products */
.grid{top:1064px;left:100px;width:1000px;display:grid;grid-template-columns:repeat(4,220px);column-gap:40px;row-gap:56px}
.card{text-align:center}
.card .thumb{width:220px;height:210px;border:1px solid var(--line);display:flex;align-items:center;justify-content:center}
.card .thumb span{display:block;width:110px;height:120px;border-radius:8px}
.card h3{font-family:"Raleway",sans-serif;font-size:14px;font-weight:700;margin-top:12px;color:#333}
.card p{font-size:11px;color:var(--muted);line-height:15px;margin-top:3px}
.card .price{font-size:15px;font-weight:700;color:var(--price);margin-top:6px}
.more{top:1860px;left:450px;width:300px;height:36px;border:1px solid #ccc;border-radius:18px;font-family:"Raleway",sans-serif;font-size:12px;font-weight:700;text-align:center;padding-top:10px;color:#444}
.more-line{top:1878px;height:1px;background:var(--line);width:340px}

/* newsletter */
.newsletter{top:1960px;left:0;width:1200px;height:160px;background:var(--cream)}
.coupon{position:absolute;left:100px;top:14px;width:130px;height:130px;border-radius:50%;background:var(--yellow);color:#fff;text-align:center;font-family:"Raleway",sans-serif;font-weight:800;padding-top:30px}
.coupon small{display:block;font-size:12px;font-weight:600}
.coupon b{display:block;font-size:40px;line-height:44px}
.news-copy{position:absolute;left:250px;top:52px;font-family:"Raleway",sans-serif;font-size:20px;font-weight:700;color:#444;line-height:26px}
.news-form{position:absolute;left:680px;top:62px;width:360px;height:36px;border:1px solid #ddd;background:#fff;border-radius:18px;font-size:12px;color:#aaa;padding:10px 0 0 18px}
.news-form i{position:absolute;right:4px;top:3px;width:28px;height:28px;border-radius:50%;background:var(--teal);color:#fff;font-style:normal;font-size:16px;text-align:center;line-height:28px}

/* footer columns */
.cols{top:2180px;left:100px;width:1000px;display:grid;grid-template-columns:repeat(4,220px);column-gap:40px}
.col h4{display:flex;align-items:center;gap:10px;font-family:"Raleway",sans-serif;font-size:22px;font-weight:600;color:#333;background:linear-gradient(90deg,#fdf5d6,#fff);padding:4px 0;margin-bottom:18px}
.col h4 .sq{width:22px;height:22px;background:var(--yellow)}
.col p{font-size:11px;color:#777;line-height:16px;margin-bottom:10px}
.store-photo{width:200px;height:150px;background:linear-gradient(135deg,#c9e3ef,#8fb7c9 55%,#e6eef2)}
.socials{display:flex;gap:8px;flex-wrap:wrap;width:150px}
.socials span{width:26px;height:26px;background:var(--teal);border-radius:3px}

/* bottom band */
.bottom{top:2472px;left:0;width:1200px;height:140px;background:var(--teal);color:#e6f4f4}
.pay{position:absolute;left:480px;top:22px;display:flex;gap:6px}
.pay span{width:38px;height:20px;background:#e7eeee;border-radius:2px}
.footlinks{position:absolute;left:0;width:1200px;top:56px;display:flex;justify-content:center;gap:38px;font-size:12px}
.copy{position:absolute;left:0;width:1200px;top:88px;text-align:center;font-size:11px;color:#cfe8e8}
.totop{position:absolute;right:40px;top:64px;font-size:14px;font-weight:700}
</style>
</head>
<body>

<header class="topbar">
  <div class="abs toplinks"><a>Check out</a><a>Log in</a><a>Register</a><a>Contact</a></div>
  <div class="abs brand"><span class="dot"></span>Brindle Corner</div>
  <div class="abs account"><span>My wishlist (0)</span><span>USD ▾</span>
    <span class="cart"><svg width="18" height="16" viewBox="0 0 18 16"><path d="M1 1h3l2 9h9l2-6H5" fill="none" stroke="#1f9aa0" stroke-width="1.6"/><circle cx="7" cy="13.5" r="1.5" fill="#1f9aa0"/><circle cx="14" cy="13.5" r="1.5" fill="#1f9aa0"/></svg>$0.00</span></div>
</header>

<nav class="abs nav">
  <ul><li class="active">HOME</li><li>DOG</li><li>CAT</li><li>FISH</li><li>BIRD</li><li>SMALL PET</li><li>CONTACT</li></ul>
  <div class="search"><svg width="12" height="12" viewBox="0 0 12 12"><circle cx="5" cy="5" r="4" fill="none" stroke="#aaa" stroke-width="1.5"/><path d="M8 8l3 3" stroke="#aaa" stroke-width="1.5"/></svg>Search here...</div>
</nav>

<section class="abs hero">
  <div class="hero-photo" role="img" aria-label="Two groomed long-haired terriers sitting side by side"></div>
  <svg class="arrow" style="left:14px" width="20" height="60" viewBox="0 0 20 60"><path d="M16 4L4 30l12 26" fill="none" stroke="#bbb" stroke-width="3"/></svg>
  <svg class="arrow" style="right:14px" width="20" height="60" viewBox="0 0 20 60"><path d="M4 4l12 26L4 56" fill="none" stroke="#bbb" stroke-width="3"/></svg>
  <div class="hero-copy">
    <h1>GROOMING PRODUCTS</h1>
    <h2>Wide Selection of Dog Grooming Products<br>Available in our store</h2>
    <div class="deal">FREE DELIVERY ON ORDERS OVER $79</div>
    <div class="tag">portable, ready, personal</div>
    <a class="btn">READ MORE</a>
  </div>
</section>

<section class="abs features">
  <div class="feature f-blue"><svg width="34" height="34" viewBox="0 0 34 34"><rect x="5" y="10" width="24" height="20" fill="none" stroke="#fff" stroke-width="2"/><path d="M11 10V6h12v4" fill="none" stroke="#fff" stroke-width="2"/></svg>Upto 5% Discount on Free Shipping</div>
  <div class="feature f-tan"><svg width="34" height="34" viewBox="0 0 34 34"><rect x="3" y="7" width="28" height="20" fill="none" stroke="#fff" stroke-width="2"/><path d="M3 13h28" stroke="#fff" stroke-width="2"/></svg>Great Customer Service</div>
  <div class="feature f-red"><svg width="34" height="34" viewBox="0 0 34 34"><rect x="2" y="10" width="18" height="14" fill="none" stroke="#fff" stroke-width="2"/><path d="M20 14h7l5 5v5H20" fill="none" stroke="#fff" stroke-width="2"/><circle cx="9" cy="27" r="3" fill="#fff"/><circle cx="26" cy="27" r="3" fill="#fff"/></svg>Free Shipping on order over $79</div>
  <div class="feature f-grey"><svg width="34" height="34" viewBox="0 0 34 34"><rect x="4" y="6" width="26" height="24" fill="none" stroke="#fff" stroke-width="2"/><path d="M4 13h26M11 3v6M23 3v6" stroke="#fff" stroke-width="2"/></svg>Delivery Schedule Spread Clear Time</div>
</section>

<section class="abs tabs">
  <span class="rule" style="left:0"></span><span class="rule" style="right:0"></span>
  <ul><li class="active">Best Sellers</li><li>New products</li><li>Best sellers</li></ul>
</section>

<section class="abs grid">
  <div class="card"><div class="thumb"><span role="img" aria-label="Dog coat product photo" style="background:#d7dde6"></span></div><h3>PRODUCT 1</h3><p>Yellow Diamond Dash<br>Water Spray</p><div class="price">$ 270.00</div></div>
  <div class="card"><div class="thumb"><span role="img" aria-label="Dog jacket product photo" style="background:#8ccf6a"></span></div><h3>PRODUCT 2</h3><p>Soft Gear Glitz<br>Eyelash Lotion</p><div class="price">$ 112.00</div></div>
  <div class="card"><div class="thumb"><span role="img" aria-label="Pet bed product photo" style="background:#a7b85c"></span></div><h3>PRODUCT 3</h3><p>Bed for Women</p><div class="price">$ 120.00</div></div>
  <div class="card"><div class="thumb"><span role="img" aria-label="Pet carrier product photo" style="background:#d63a3a"></span></div><h3>PRODUCT 4</h3><p>Yellow Diamond Dash<br>Water Spray</p><div class="price">$ 20.00</div></div>
  <div class="card"><div class="thumb"><span role="img" aria-label="Chain leash product photo" style="background:#cfcfcf"></span></div><h3>PRODUCT 5</h3><p>Yellow Diamond Dash<br>Water Spray</p><div class="price">$ 270.00</div></div>
  <div class="card"><div class="thumb"><span role="img" aria-label="Cat tree product photo" style="background:#c9b79a"></span></div><h3>PRODUCT 6</h3><p>Soft Gear Glitz<br>Eyelash Lotion</p><div class="price">$ 112.00</div></div>
  <div class="card"><div class="thumb"><span role="img" aria-label="Dog dress product photo" style="background:#e7b3b9"></span></div><h3>PRODUCT 7</h3><p>Bed for Women</p><div class="price">$ 120.00</div></div>
  <div class="card"><div class="thumb"><span role="img" aria-label="Leash reel product photo" style="background:#333"></span></div><h3>PRODUCT 8</h3><p>Yellow Diamond Dash<br>Water Spray</p><div class="price">$ 20.00</div></div>
</section>

<span class="abs more-line" style="left:100px"></span><span class="abs more-line" style="left:760px"></span>
<a class="abs more">LOAD MORE PRODUCTS</a>

<section class="abs newsletter">
  <div class="coupon"><small>GET A</small><b>$10</b><small>COUPON</small></div>
  <div class="news-copy">Sign in to our newsletter and<br>receive a ten dollars coupon</div>
  <div class="news-form">Enter your email address<i>+</i></div>
</section>

<section class="abs cols">
  <div class="col"><h4><span class="sq"></span>Our Store</h4><div class="store-photo" role="img" aria-label="Groomed small dog at the store"></div></div>
  <div class="col"><h4><span class="sq"></span>About</h4>
    <p>Our shop brings carefully chosen food, toys and grooming care to pets of every size, with friendly advice from people who love animals.</p>
    <p>We pack each order with care and ship it quickly, so your dog, cat, bird or fish gets what it needs right on time.</p></div>
  <div class="col"><h4><span class="sq"></span>Follow us</h4><div class="socials"><span></span><span></span><span></span><span></span><span></span><span></span></div></div>
  <div class="col"><h4><span class="sq"></span>Contact us</h4>
    <p>22 Elm Street, Suite 4<br>Springfield<br>(555) 014-2290<br>hello@brindlecorner.com<br>brindlecorner.com</p></div>
</section>

<footer class="abs bottom">
  <div class="pay"><span></span><span></span><span></span><span></span><span></span><span></span></div>
  <div class="footlinks"><a>Home</a><a>Blog</a><a>Shop</a><a>Wishlist</a><a>Products</a><a>Brand</a><a>Contact Us</a></div>
  <div class="copy">Copyright © 2024 Brindle Corner</div>
  <div class="totop">▲</div>
</footer>

</body>
</html>
```